Design using coins, gold & slver

We primarily buy, sell and trade Rare U.S. Coins, Gold Bullion and Silver. We are located in Minnetonka, Minnesota which is known for an upscale lake lifestyle (some logos associated with Minnetonka are anchors and sailboats). We sell throughout the U.S.Colors are not determined yet, however, Navy blue may be good with gold, but we're open to other combinations.
Updates

Project Deadline Extended
Reason: The designer of my first choice has not responded in over 2-days. I may need one more design

Target Market(s)

Coin Collectors

Industry/Entity Type

Trade

Contact Information for Business Card

Gerald Pastwick, CEO, Professional NumismatistMinnetonka Rare Coin and BullionP.O.Box 127 - Larkmere, MN 55391-0127 (p) 612.555.0148 (fax): 952.555.0173
HarrowdaleRareCoin1@examplemail.net

Font styles to use
Serif

Colors
0555a3
ffc214
85abd2

Requirements
Nice to have
• Enclosed samples of other business cards in the same business
• Enclosed some sample images

```html
<!DOCTYPE html>
<html lang="en">
<head>
<meta charset="utf-8">
<title>Harrowdale Rare Coin and Bullion – Business Card</title>
<link rel="stylesheet" href="https://fonts.googleapis.com/css2?family=Libre+Caslon+Text:ital,wght@0,400;0,700;1,400&display=swap">
<style>
  :root {
    --sky: #85abd2;
    --navy: #0555a3;
    --gold: #ffc214;
    --gold-mid: #e9a90f;
    --gold-deep: #c98f0a;
    --white: #ffffff;
  }
  * { margin: 0; padding: 0; box-sizing: border-box; }
  html, body { width: 1200px; height: 702px; overflow: hidden; background: var(--sky); }
  .card {
    position: relative;
    width: 1200px;
    height: 702px;
    overflow: hidden;
    background: var(--sky);
    font-family: "Libre Caslon Text", Georgia, serif;
    font-variant-ligatures: no-common-ligatures no-discretionary-ligatures no-historical-ligatures;
    color: var(--white);
  }
  .card__wave { position: absolute; inset: 0; width: 1200px; height: 702px; }
  .brand {
    position: absolute;
    left: 105px;
    top: 61px;
    display: flex;
    align-items: center;
    gap: 34px;
  }
  .brand__disc {
    width: 380px;
    height: 380px;
    border-radius: 50%;
    background: radial-gradient(circle at 40% 35%, var(--gold) 0%, var(--gold-mid) 60%, var(--gold-deep) 100%);
  }
  .brand__name {
    font-weight: 700;
    font-size: 32px;
    line-height: 1.25;
    color: var(--navy);
  }
  .company {
    position: absolute;
    left: 58px;
    top: 486px;
    font-size: 29px;
    line-height: 44px;
  }
  .company__name { font-weight: 700; }
  .contact {
    position: absolute;
    right: 58px;
    top: 364px;
    text-align: right;
  }
  .contact__name { font-weight: 700; font-size: 40px; line-height: 46px; }
  .contact__role { font-weight: 700; font-size: 30px; line-height: 42px; }
  .contact__title { font-style: italic; font-size: 28px; line-height: 46px; }
  .contact__line { font-size: 28px; line-height: 54px; }
  .contact__number { font-weight: 700; font-size: 38px; margin-left: 12px; }
  .contact__email { font-size: 27px; line-height: 46px; }
</style>
</head>
<body>
<div class="card">
  <svg class="card__wave" viewBox="0 0 1200 702" aria-hidden="true">
    <path d="M0,376 C150,440 280,470 420,452 C600,425 760,305 940,292 C1060,284 1150,298 1200,310 L1200,702 L0,702 Z" fill="var(--navy)"/>
  </svg>

  <div class="brand">
    <div class="brand__disc" aria-hidden="true"></div>
    <div class="brand__name">Harrowdale<br>Rare Coin and Bullion</div>
  </div>

  <div class="company">
    <div class="company__name">Harrowdale Rare</div>
    <div class="company__name">Coin and Bullion</div>
    <div class="company__address">P.O. Box 482</div>
    <div class="company__address">Larkmere, MN 55391</div>
  </div>

  <div class="contact">
    <div class="contact__name">Gerald Pastwick</div>
    <div class="contact__role">CEO</div>
    <div class="contact__title">Professional Numismatist</div>
    <div class="contact__line">(phone)<span class="contact__number">612.555.0148</span></div>
    <div class="contact__line">(fax)<span class="contact__number">952.555.0173</span></div>
    <div class="contact__email">HarrowdaleRareCoin1@examplemail.net</div>
  </div>
</div>
</body>
</html>
```